Fernhollow Landscaping Folder Design

I need a graphic designer to design a folder so we can insert informational sheets inside it for customers. The folder must include the company logo, project images, on front and back of folder and slogan " The Experience You Want, The Service You Expect, And The Value You Deserve'

Folder to also include phone numbers : 416 555 0187 as well as the website: www.fernhollowlandscaping.example as well as we gurantee a 24 month warranty.

I have attached sample of size we need.

Pixel Bazaar has also done something similar for me for Tillwood Landscapes

geared toward home owners & commercial/industrial

Landscaping

• open to new trendy font

• Telephone Number, email address, slogan, images,
• images of completed projects incorporated into the front and back of folder as well as the logo
• n/a

```html
<!DOCTYPE html>
<html lang="en">
<head>
<meta charset="utf-8">
<title>Fernhollow Landscaping Folder</title>
<link href="https://fonts.googleapis.com/css2?family=Lato:wght@400;700;900&family=Roboto+Condensed:wght@700&display=swap" rel="stylesheet">
<style>
  :root {
    --backdrop: #6e6e6e;
    --brand-blue: #1a6fd0;
    --bright-blue: #1e8cf0;
    --deep-navy: #0b2b52;
    --silver: #e9e9ea;
    --ink: #2a2a2a;
    --white: #ffffff;
  }
  html, body { margin: 0; padding: 0; overflow: hidden; }
  body { width: 1200px; height: 907px; background: var(--backdrop); }
  .canvas { position: relative; width: 1200px; height: 907px; }
  .folder-art { position: absolute; inset: 0; }
  .warranty {
    position: absolute; left: 422px; top: 322px;
    font-family: "Roboto Condensed", "Arial Narrow", sans-serif; font-weight: 700;
    color: var(--ink);
  }
  .warranty-intro { font-size: 17px; line-height: 1; letter-spacing: -0.2px; }
  .warranty-figure { display: flex; align-items: center; margin-top: 2px; color: var(--brand-blue); }
  .warranty-number { font-size: 50px; line-height: 1; letter-spacing: -2px; }
  .warranty-term { font-size: 21px; line-height: 0.95; margin-left: 3px; letter-spacing: -0.5px; }
  .back-brand {
    position: absolute; left: 172px; top: 452px;
    font-family: "Lato", sans-serif; font-weight: 700; font-size: 12px;
    color: #555; display: flex; align-items: center; gap: 6px;
  }
  .back-brand .mark { width: 9px; height: 9px; background: #555; }
  .contact-list {
    position: absolute; left: 171px; top: 498px; margin: 0; padding: 0; list-style: none;
    font-family: "Lato", sans-serif; font-size: 9.5px; line-height: 12px; color: var(--ink);
  }
  .contact-list li { display: flex; gap: 5px; margin-bottom: 2px; }
  .contact-list svg { flex: none; width: 8px; height: 9px; margin-top: 2px; fill: var(--ink); }
  .front-brand {
    position: absolute; left: 603px; top: 448px;
    font-family: "Lato", sans-serif; font-weight: 900; font-size: 19px;
    color: var(--white); display: flex; align-items: center; gap: 8px; letter-spacing: 0.5px;
  }
  .front-brand .mark { width: 12px; height: 12px; border-radius: 50%; background: var(--white); }
  .slogan {
    position: absolute; left: 602px; top: 510px; margin: 0;
    font-family: "Lato", sans-serif; font-weight: 400; color: var(--white);
  }
  .slogan span { display: block; }
  .slogan .line-1 { font-size: 21px; line-height: 29px; }
  .slogan .line-2, .slogan .line-3 { font-size: 24px; line-height: 30px; }
  .slogan b { font-weight: 700; }
</style>
</head>
<body>
<div class="canvas">
  <svg class="folder-art" width="1200" height="907" viewBox="0 0 1200 907" aria-hidden="false">
    <defs>
      <clipPath id="folder-shape">
        <path d="M150,55 H1023 V830 H610 L588,640 L545,830 H150 Z"/>
      </clipPath>
      <linearGradient id="silver-panel" x1="0" y1="0" x2="1" y2="0">
        <stop offset="0" stop-color="#d8d8da"/>
        <stop offset="0.45" stop-color="#ffffff"/>
        <stop offset="1" stop-color="#d4d5d8"/>
      </linearGradient>
      <linearGradient id="front-blue" x1="0" y1="0" x2="1" y2="1">
        <stop offset="0" stop-color="#1e7fe0"/>
        <stop offset="1" stop-color="#1462b8"/>
      </linearGradient>
      <linearGradient id="pocket-right" x1="0" y1="0" x2="1" y2="0">
        <stop offset="0" stop-color="#1565c0"/>
        <stop offset="0.55" stop-color="#2a8ff0"/>
        <stop offset="1" stop-color="#1565c0"/>
      </linearGradient>
      <linearGradient id="driveway-tones" x1="0" y1="0" x2="0" y2="1">
        <stop offset="0" stop-color="#4d6a3a"/>
        <stop offset="0.5" stop-color="#a9aaa4"/>
        <stop offset="1" stop-color="#6c6c6a"/>
      </linearGradient>
      <linearGradient id="pool-tones" x1="0" y1="0" x2="0" y2="1">
        <stop offset="0" stop-color="#7a5a40"/>
        <stop offset="0.45" stop-color="#2f6fd6"/>
        <stop offset="1" stop-color="#6e6560"/>
      </linearGradient>
      <radialGradient id="walkway-tones">
        <stop offset="0" stop-color="#c9c6c0"/>
        <stop offset="1" stop-color="#6c7a4a"/>
      </radialGradient>
    </defs>

    <g clip-path="url(#folder-shape)">
      <rect class="front-field" x="150" y="55" width="873" height="775" fill="url(#front-blue)"/>

      <path class="back-panel" d="M150,55 H588 V410 C505,432 410,510 352,632 H150 Z" fill="url(#silver-panel)"/>
      <path class="back-swoosh" d="M588,410 C560,420 520,440 490,460 C540,430 570,420 588,418 Z" fill="#7fc0ff"/>
      <path class="back-sweep" d="M352,632 C400,520 480,450 588,418 V436 C500,460 420,530 378,632 Z" fill="#1e8cf0"/>

      <path class="driveway-arc" d="M470,55 C478,230 380,372 170,388" fill="none" stroke="#1e8cf0" stroke-width="10"/>
      <path class="driveway-photo" role="img" aria-label="Photo of a curved concrete driveway with trees and a house"
            d="M150,55 H465 C468,225 365,368 150,380 Z" fill="url(#driveway-tones)" stroke="#ffffff" stroke-width="3"/>

      <path class="pool-photo" role="img" aria-label="Photo of a backyard pool with stone waterfall and interlock patio"
            d="M588,55 H1000 C990,190 935,245 860,262 C760,285 660,350 588,406 Z" fill="url(#pool-tones)"/>
      <path class="pool-edge" d="M588,406 C660,350 760,287 860,264 C935,247 990,190 1001,55" fill="none" stroke="#ffffff" stroke-width="4"/>
      <path class="front-swoosh" d="M1005,55 H1023 V140 C1000,220 960,250 905,262 C960,235 995,170 1005,55 Z" fill="#2a95ff"/>

      <circle class="walkway-frame" cx="900" cy="355" r="106" fill="#ffffff"/>
      <circle class="walkway-photo" role="img" aria-label="Photo of a stone walkway with steps and garden plantings"
              cx="900" cy="355" r="99" fill="url(#walkway-tones)"/>

      <rect class="pocket-back" x="150" y="632" width="438" height="198" fill="var(--deep-navy)"/>
      <path class="pocket-back-sweep" d="M280,632 H588 V830 H430 C410,760 360,680 280,632 Z" fill="#1462b8"/>
      <path class="pocket-back-highlight" d="M280,632 C360,680 405,760 425,830 H440 C420,755 370,675 300,632 Z" fill="#2a8ff0"/>
      <rect class="pocket-front" x="588" y="632" width="435" height="198" fill="url(#pocket-right)"/>
      <line class="pocket-fold" x1="150" y1="632" x2="1023" y2="632" stroke="#0d4c94" stroke-width="1"/>
    </g>
  </svg>

  <div class="warranty">
    <div class="warranty-intro">We guarantee a</div>
    <div class="warranty-figure">
      <span class="warranty-number">24</span>
      <span class="warranty-term">month<br>warranty</span>
    </div>
  </div>

  <div class="back-brand"><span class="mark"></span>Fernhollow Landscaping</div>

  <ul class="contact-list">
    <li><svg viewBox="0 0 8 10"><path d="M4,0 C6.2,0 8,1.7 8,3.8 C8,6.5 4,10 4,10 C4,10 0,6.5 0,3.8 C0,1.7 1.8,0 4,0 Z"/></svg>
      <span>2250 Alder Ridge Road, Unit 4<br>Brookfield, Ontario<br>L9Z 0B7</span></li>
    <li><svg viewBox="0 0 8 9"><path d="M1.5,0 L3,2.4 L2,3.4 C2.6,4.8 3.4,5.7 4.7,6.4 L5.7,5.4 L8,7 L7,9 C3,8.6 0.2,5.4 0,1 Z"/></svg>
      <span>(416) 555-0187</span></li>
    <li><svg viewBox="0 0 8 9"><rect x="0" y="2" width="8" height="5.5"/></svg>
      <span>info@fernhollowlandscaping.example</span></li>
    <li><svg viewBox="0 0 8 9"><circle cx="4" cy="4.5" r="3.6"/></svg>
      <span>www.fernhollowlandscaping.example</span></li>
  </ul>

  <div class="front-brand"><span class="mark"></span>Fernhollow Landscaping</div>

  <p class="slogan">
    <span class="line-1">The experience you <b>Want</b></span>
    <span class="line-2">The service you <b>Expect</b></span>
    <span class="line-3">&amp; The value you <b>Deserve</b></span>
  </p>
</div>
</body>
</html>
```